Clara Joy Halden- Lantern Waltz- Autumn/Winter Tour Dates

I need high res A3 Tour poster for print and for social media JPG sharing of tour dates.
Also needed Facebook/Twitter Banner Cover Photos of these dates.
Text Needed Below
Clara Joy Halden
Lantern Waltz
Autumn/Winter Tour Dates
03/09 Ravensby Folk Festival
21/09 Swindon- Calder Theatre
01/10 Hitchin- Brackwell Folk Club
17/10 Bath- The Anvil
20/10 Sheffield- Upper Dale Croquet Club
24/10 Birmingham- Orchard Lamp Cafe
26/10 Glasgow- The Nook and Jar
27/10 Edinburgh - The Marble Parlour
08/11 Capital Reel and Ballad Festival- The Crooked Heron
25/11 Lewes- Tandem Record Shop- Live In Store
02/12 Cambridge- The Quayside
27/01 Lincolnshire- Fenmarsh Theatre
Tickets/Info: www.clarajoyhalden-music.example/gigs
(Quotes/Reviews To Put On)
"Outstanding, rich and expressive."            "Vibrant and Experimental"
**** BdM                                                               **** Tunepaths
"Impressive and Invigorating"                        "Enchanting" Acoustic Wire UK
tBarks

Updates
I cannot read the tour dates on most of the submissions so far. They need to be visible to viewers.
Thank You.
Please also be as creative and inventive as possible- not bland.

Target Market(s)
Music Fans- Folk Acoustic Americana
Industry/Entity Type
Media
Font styles to use
Requirements
Must have
- My photo featured prominently
- Look classy and not tacky or OTT
- Look elegant, wintery and eye catching
- The dates must be very clear to read
- Links to Website:

Nice to have
- Something innovative and not boring in terms of layout design
- Perhaps fading/ misty or wintery

Should not have
- Any colours that do not match

```html
<!DOCTYPE html>
<html lang="en">
<head>
<meta charset="utf-8">
<title>Clara Joy Halden – Lantern Waltz – Autumn/Winter Tour Dates</title>
<link rel="stylesheet" href="https://fonts.googleapis.com/css2?family=Sofia&display=swap">
<style>
  :root {
    --page-white: #ffffff;
    --frost-blue: #88aad5;
    --frost-blue-light: #9cbbe0;
    --snow: #f4f8fd;
    --ink-shadow: rgba(28, 44, 78, 0.75);
    --ornament-tone: #dfe9f6;
    --photo-dark: #1c2230;
    --photo-mid: #4a5468;
    --band-fill: #c9d9ee;
    --band-edge: #5b7196;
  }
  * { margin: 0; padding: 0; box-sizing: border-box; }
  html, body {
    width: 1200px; height: 1000px; overflow: hidden;
    background: var(--page-white);
  }
  .poster {
    position: absolute; left: 269px; top: 0;
    width: 708px; height: 1000px;
    background: radial-gradient(ellipse at 50% 40%, var(--frost-blue-light), var(--frost-blue) 70%);
    overflow: hidden;
    font-family: "Sofia", cursive;
    color: var(--snow);
  }
  .script-text {
    position: absolute; left: 0; width: 100%;
    text-align: center; white-space: nowrap; font-weight: 400;
    text-shadow: 1px 1px 0 var(--ink-shadow), 2px 3px 4px var(--ink-shadow);
  }
  .artist-name { top: 26px; font-size: 44px; z-index: 2; }
  .album-title { top: 98px; font-size: 44px; z-index: 2; }
  .tour-heading { top: 400px; font-size: 34px; z-index: 2; }
  .artist-photo {
    position: absolute; left: 246px; top: 95px; width: 220px; height: 315px;
    background: radial-gradient(ellipse at 50% 40%, var(--photo-mid), var(--photo-dark) 75%);
    box-shadow: 0 0 14px 6px rgba(230, 238, 250, 0.6);
  }
  .side-ornament {
    position: absolute; top: 0; width: 95px; height: 375px;
    background: linear-gradient(to bottom, var(--ornament-tone), rgba(223,233,246,0.55));
    opacity: 0.55; border-radius: 0 0 40px 40px;
  }
  .side-ornament.left { left: 36px; }
  .side-ornament.right { left: 581px; }
  .leaf-flourish {
    position: absolute; top: 362px; width: 42px; height: 72px;
    background: var(--ornament-tone); opacity: 0.6; border-radius: 50% 50% 40% 40%;
  }
  .leaf-flourish.left { left: 104px; }
  .leaf-flourish.right { left: 571px; }
  .divider { position: absolute; left: 68px; width: 582px; height: 30px; }
  .divider.top { top: 448px; }
  .divider.bottom { top: 874px; }
  .tour-dates {
    position: absolute; top: 468px; left: 0; width: 100%;
    list-style: none;
  }
  .tour-dates li {
    height: 34px; line-height: 34px; font-size: 22px;
    text-align: center; white-space: nowrap;
    text-shadow: 1px 1px 0 var(--ink-shadow), 2px 2px 3px var(--ink-shadow);
  }
  .tour-dates li.long-line { font-size: 20px; }
  .press-quotes {
    position: absolute; top: 906px; left: 30px; width: 648px;
    display: grid; grid-template-columns: 1fr 1fr; row-gap: 2px;
    list-style: none;
  }
  .press-quotes li {
    font-size: 15px; line-height: 20px; text-align: center; white-space: nowrap;
    text-shadow: 1px 1px 0 var(--ink-shadow), 1px 2px 3px var(--ink-shadow);
  }
  .tickets-info {
    position: absolute; top: 956px; left: 0; width: 100%;
    font-size: 18px; line-height: 26px; text-align: center; white-space: nowrap;
    text-shadow: 1px 1px 0 var(--ink-shadow), 2px 2px 3px var(--ink-shadow);
  }
</style>
</head>
<body>
  <main class="poster">
    <div class="side-ornament left" role="img" aria-label="Frosted vertical floral ornament column"></div>
    <div class="side-ornament right" role="img" aria-label="Frosted vertical floral ornament column"></div>

    <h1 class="script-text artist-name">Clara Joy Halden</h1>
    <div class="artist-photo" role="img" aria-label="Portrait photo of the artist in a wintry crown, framed in frost"></div>
    <h2 class="script-text album-title">Lantern Waltz</h2>

    <div class="leaf-flourish left" role="img" aria-label="Frosted leaf flourish"></div>
    <div class="leaf-flourish right" role="img" aria-label="Frosted leaf flourish"></div>
    <h3 class="script-text tour-heading">Autumn/Winter Tour Dates</h3>

    <svg class="divider top" viewBox="0 0 582 30" aria-hidden="true">
      <path d="M4 6 Q10 14 18 12 L564 12 Q572 14 578 6" fill="none" stroke="var(--band-edge)" stroke-width="2"/>
      <rect x="18" y="12" width="546" height="9" rx="4" fill="var(--band-fill)" stroke="var(--band-edge)" stroke-width="1.5"/>
      <path d="M4 24 Q10 22 18 21 M564 21 Q572 22 578 24" fill="none" stroke="var(--band-edge)" stroke-width="2"/>
    </svg>

    <ul class="tour-dates">
      <li>03/09 Ravensby Folk Festival</li>
      <li>21/09 Swindon- Calder Theatre</li>
      <li>01/10 Hitchin- Brackwell Folk Club</li>
      <li>17/10 Bath- The Anvil</li>
      <li>20/10 Sheffield- Upper Dale Croquet Club</li>
      <li>24/10 Birmingham- Orchard Lamp Cafe</li>
      <li>26/10 Glasgow- The Nook and Jar</li>
      <li>27/10 Edinburgh - The Marble Parlour</li>
      <li class="long-line">08/11 Capital Reel and Ballad Festival- The Crooked Heron</li>
      <li>25/11 Lewes- Tandem Record Shop- Live In Store</li>
      <li>02/12 Cambridge- The Quayside</li>
      <li>27/01 Lincolnshire- Fenmarsh Theatre</li>
    </ul>

    <svg class="divider bottom" viewBox="0 0 582 30" aria-hidden="true">
      <path d="M4 6 Q10 14 18 12 L564 12 Q572 14 578 6" fill="none" stroke="var(--band-edge)" stroke-width="2"/>
      <rect x="18" y="12" width="546" height="9" rx="4" fill="var(--band-fill)" stroke="var(--band-edge)" stroke-width="1.5"/>
      <path d="M4 24 Q10 22 18 21 M564 21 Q572 22 578 24" fill="none" stroke="var(--band-edge)" stroke-width="2"/>
    </svg>

    <ul class="press-quotes">
      <li>“Outstanding, rich and expressive.” **** BdM</li>
      <li>“Vibrant and Experimental” **** Tunepaths</li>
      <li>“Impressive and Invigorating” tBarks</li>
      <li>“Enchanting” Acoustic Wire UK</li>
    </ul>

    <p class="tickets-info">Tickets/Info: www.clarajoyhalden-music.example/gigs</p>
  </main>
</body>
</html>
```